Business Card Design Project

Use newly designed logo and tie into newly designed website
I need a new logo and website layout designed for my partner's business. This is a birthday present. His business is interior painting, wallpapering and design. He also has access to a wide variety of products including carpet, fabrics, furniture, wallpaper, tile, countertops, etc. I have attached some screen shots of his website for reference. He is a one man shop and has a stellar reputation with his customers. He is on-time, very tidy, excellent with animals, and always finishes on time and on budget. There are no restrictions on colors or fonts. The logo needs to work well with the website, business cards and printed materials. The website needs to flow content for device size so it looks just as good on a cell phone or tablet as it does on a desktop computer. Whatever the heck that's called!Thanks. I am looking forward to seeing everyone's ideas.
Target Market(s)
Consumers looking to improve the interior environment of their homes by updating wall paint or paper, flooring (either carpet, tile, or hardwoods), counter tops, window treatments, etc. Clients tend to be more upper middle class and have certain taste levels and expectations. New logo, website and business card should align to meet those levels.
Industry/Entity Type
Cell Phone
Look and feel

```html
<!DOCTYPE html>
<html lang="en">
<head>
<meta charset="utf-8">
<title>Marento Interior Designs – Business Card</title>
<link href="https://fonts.googleapis.com/css2?family=Questrial&display=swap" rel="stylesheet">
<style>
  :root {
    --page-bg: #e6e3df;
    --card-bg: #ffffff;
    --navy: #23204a;
    --burgundy: #8c1d1d;
    --orange: #e58a1c;
    --taupe: #9a8a64;
    --ink: #2b2b2b;
  }
  * { box-sizing: border-box; margin: 0; padding: 0; }
  html, body {
    width: 1200px; height: 900px; overflow: hidden;
    background: var(--page-bg);
    font-family: "Questrial", "Century Gothic", sans-serif;
  }
  .business-card {
    position: absolute;
    left: 180px; top: 210px;
    width: 840px; height: 480px;
    background: var(--card-bg);
    border-radius: 22px;
    box-shadow: 0 10px 30px rgba(0,0,0,.18);
    overflow: hidden;
  }
  .brand {
    position: absolute;
    left: 120px; top: 150px;
    width: 300px;
    color: var(--navy);
  }
  .brand-row { display: flex; align-items: center; gap: 14px; }
  .brand-square {
    width: 44px; height: 44px;
    background: var(--navy);
  }
  .brand-name {
    font-size: 50px; letter-spacing: 1px; line-height: 1;
    text-transform: uppercase;
  }
  .brand-tagline {
    margin-top: 6px;
    font-size: 21px; letter-spacing: 2px;
    text-transform: uppercase;
  }
  .brand-url {
    position: absolute;
    left: 120px; top: 340px;
    font-size: 20px; color: var(--ink);
    letter-spacing: .5px;
  }
  .person {
    position: absolute;
    left: 465px; top: 115px;
  }
  .person-name {
    font-size: 36px; color: var(--burgundy);
    letter-spacing: .5px;
  }
  .contact-list {
    list-style: none;
    margin-top: 26px; margin-left: 60px;
    font-size: 15px; color: var(--ink); line-height: 1.45;
  }
  .contact-item { display: flex; align-items: flex-start; gap: 12px; }
  .contact-icon { width: 12px; height: 12px; margin-top: 4px; flex: none; fill: var(--taupe); }
</style>
</head>
<body>
  <section class="business-card" aria-label="Business card">
    <div class="brand">
      <div class="brand-row">
        <span class="brand-square"></span>
        <span class="brand-name">Marento</span>
      </div>
      <div class="brand-tagline">Interior Designs</div>
    </div>
    <div class="brand-url">www.marentodesigns.com</div>

    <div class="person">
      <h1 class="person-name">Dale Marento</h1>
      <ul class="contact-list">
        <li class="contact-item">
          <svg class="contact-icon" viewBox="0 0 12 12" aria-hidden="true"><path d="M2 1h3l1 3-2 1a7 7 0 0 0 3 3l1-2 3 1v3c-6 1-10-3-9-9z"/></svg>
          <span>(913) 555-0142</span>
        </li>
        <li class="contact-item">
          <svg class="contact-icon" viewBox="0 0 12 12" aria-hidden="true"><path d="M1 2h10v8H1z M1 2l5 4 5-4" fill="none" stroke="#9a8a64" stroke-width="1.4"/></svg>
          <span>dale@marentodesigns.com</span>
        </li>
        <li class="contact-item">
          <svg class="contact-icon" viewBox="0 0 12 12" aria-hidden="true"><path d="M6 0a4 4 0 0 1 4 4c0 3-4 8-4 8S2 7 2 4a4 4 0 0 1 4-4zm0 2.5a1.5 1.5 0 1 0 0 3 1.5 1.5 0 0 0 0-3z"/></svg>
          <span>2048 W Aspen Ct.<br>Linwood, KS 66052</span>
        </li>
      </ul>
    </div>
  </section>
</body>
</html>
```